Advert for Services that we offer

Bolt Remova Ltd need an design to represent what we do in a modern way by showing an image with a brief description and the use of corporate logo the information we will proved vie a doc file and this is to be presented in a modern way. This design will be for print & web. we have done our own design and its not great i have put this in the file repository

Target Market(s)

Motor trade

Font styles to use
Sans Serif

Colors

Designer to choose colors to be used in the design.

Requirements
Must have
• Company colour scheme as per logo within the files uploaded.
• and a small boarder to isolate it from the rest of the articles.
Nice to have
• Modern font
Should not have
• Old style font

```html
<!DOCTYPE html>
<html lang="en">
<head>
<meta charset="utf-8">
<title>Bolt Remova Ltd – Product Testing &amp; Analysis</title>
<link href="https://fonts.googleapis.com/css2?family=Orbitron:wght@900&family=Montserrat:wght@600;700&display=swap" rel="stylesheet">
<style>
  :root {
    --backdrop: #a7a8ab;
    --frame-blue: #1f74bd;
    --title-blue: #17609f;
    --accent-blue: #1e78c8;
    --paper: #ffffff;
    --ink: #333333;
    --pill: #dcdcdc;
    --divider: #c4c4c4;
  }
  html, body {
    margin: 0;
    width: 1200px;
    height: 775px;
    overflow: hidden;
    background: var(--backdrop);
  }
  .stage {
    position: absolute;
    left: 0; top: 0;
    width: 1529px;
    height: 987px;
    transform: scale(0.7848);
    transform-origin: 0 0;
  }
  .advert {
    position: absolute;
    left: 339px; top: 219px;
    width: 850px; height: 549px;
    background: var(--frame-blue);
  }
  .advert-inner {
    position: absolute;
    left: 14px; top: 14px;
    width: 823px; height: 522px;
    background: var(--paper);
    overflow: hidden;
  }
  .photo {
    position: absolute;
    left: 0; top: 0;
    width: 823px; height: 522px;
  }
  .headline {
    position: absolute;
    left: 43px; top: 40px;
    margin: 0;
    font-family: "Orbitron", sans-serif;
    font-weight: 900;
    font-size: 47px;
    line-height: 41px;
    letter-spacing: -1px;
    color: var(--title-blue);
    text-transform: uppercase;
  }
  .services {
    position: absolute;
    left: 52px; top: 189px;
    margin: 0; padding: 0;
    list-style: none;
  }
  .services li {
    display: flex;
    align-items: center;
    width: 400px;
    height: 36px;
    margin-bottom: 9.8px;
    padding-left: 10px;
    border-radius: 18px 0 0 18px;
    background: linear-gradient(90deg, var(--pill) 0%, #f1f1f1 60%, rgba(255,255,255,0) 100%);
    font-family: "Montserrat", sans-serif;
    font-weight: 700;
    font-size: 24px;
    color: var(--ink);
    letter-spacing: 0.3px;
  }
  .services svg {
    width: 23px; height: 23px;
    margin-right: 3px;
    flex: none;
  }
  .divider {
    position: absolute;
    left: 416px; top: 181px;
    width: 3px; height: 80px;
    background: var(--divider);
  }
  .brand {
    position: absolute;
    left: 430px; top: 220px;
    display: flex;
    align-items: center;
    gap: 6px;
    font-family: "Montserrat", sans-serif;
    font-weight: 700;
    font-size: 15px;
    color: var(--accent-blue);
    white-space: nowrap;
  }
  .brand-mark {
    width: 14px; height: 14px;
    background: var(--accent-blue);
  }
  .call {
    position: absolute;
    left: 43px; top: 423px;
    margin: 0;
    font-family: "Orbitron", sans-serif;
    font-weight: 900;
    font-size: 31px;
    color: var(--accent-blue);
    letter-spacing: 0.5px;
    white-space: nowrap;
  }
  .web {
    position: absolute;
    left: 44px; top: 459px;
    margin: 0;
    font-family: "Montserrat", sans-serif;
    font-weight: 700;
    font-size: 18px;
    color: var(--accent-blue);
  }
</style>
</head>
<body>
<div class="stage">
  <section class="advert">
    <div class="advert-inner">
      <svg class="photo" viewBox="0 0 823 522" role="img" aria-label="Photo of a technician measuring the bore of a red-painted flanged bearing housing with a digital gauge">
        <defs>
          <linearGradient id="photoTone" x1="0" y1="0" x2="1" y2="1">
            <stop offset="0" stop-color="#6e6b68"/>
            <stop offset="0.45" stop-color="#3e4043"/>
            <stop offset="0.7" stop-color="#8a4a2a"/>
            <stop offset="1" stop-color="#2f3134"/>
          </linearGradient>
        </defs>
        <path d="M453,0 L823,0 L823,522 L440,522 C450,380 520,270 670,232 C560,220 470,130 453,0 Z" fill="url(#photoTone)"/>
      </svg>

      <h1 class="headline">Product<br>Testing &amp;<br>Analysis</h1>

      <ul class="services">
        <li><svg viewBox="0 0 24 24"><path d="M12 2.5l2.8 6.2 6.7.6-5.1 4.4 1.6 6.6L12 16.8 6 20.3l1.6-6.6L2.5 9.3l6.7-.6z" fill="none" stroke="#1e78c8" stroke-width="2.2" stroke-linejoin="round"/></svg>Metallurgical testing</li>
        <li><svg viewBox="0 0 24 24"><path d="M12 2.5l2.8 6.2 6.7.6-5.1 4.4 1.6 6.6L12 16.8 6 20.3l1.6-6.6L2.5 9.3l6.7-.6z" fill="none" stroke="#1e78c8" stroke-width="2.2" stroke-linejoin="round"/></svg>Bearing pre-load testing</li>
        <li><svg viewBox="0 0 24 24"><path d="M12 2.5l2.8 6.2 6.7.6-5.1 4.4 1.6 6.6L12 16.8 6 20.3l1.6-6.6L2.5 9.3l6.7-.6z" fill="none" stroke="#1e78c8" stroke-width="2.2" stroke-linejoin="round"/></svg>Bore measurement</li>
        <li><svg viewBox="0 0 24 24"><path d="M12 2.5l2.8 6.2 6.7.6-5.1 4.4 1.6 6.6L12 16.8 6 20.3l1.6-6.6L2.5 9.3l6.7-.6z" fill="none" stroke="#1e78c8" stroke-width="2.2" stroke-linejoin="round"/></svg>New product evaluation</li>
        <li><svg viewBox="0 0 24 24"><path d="M12 2.5l2.8 6.2 6.7.6-5.1 4.4 1.6 6.6L12 16.8 6 20.3l1.6-6.6L2.5 9.3l6.7-.6z" fill="none" stroke="#1e78c8" stroke-width="2.2" stroke-linejoin="round"/></svg>Product analysis &amp; report</li>
      </ul>

      <div class="divider"></div>
      <div class="brand"><span class="brand-mark"></span>Bolt Remova Ltd</div>

      <p class="call">CALL: 0161 555 0192</p>
      <p class="web">www.bolt-remova.co.uk</p>
    </div>
  </section>
</div>
</body>
</html>
```